Tilda and Rook Competition Poster.

Hi Deigners,
I need to help to design a poster for a competition.
Details for competition is exactly the same as my previous design but simply change the name to TILDA & ROOK.
Competition will start : 1st AUGUST 2017
Competion end : 31st AUGUST 2017
Poster name: TILDA & ROOK BREEZE COMPETITION
Poster Description:
WIN a $100 Food Voucher
Share your photos on SNAPBOARD or LENSLY to WIN.
To Enter, Simply:
1. Like our Snapboard page or follow us on Lensly
2. Take an original photo of any item(s) of our food
3. Post your photo(s) to our Snapboard page or Lensly page, must use hashtags #tildaandrook #tildaandbreeze
4. Be as creative as you'd like, and the TWO BEST photos voted by the Tilda and Rook team will receive a $100 Food Voucher.
I've also attached the Terms & Conditions, Please Copy and Paste these terms but must replace it with the updated details.
Good Luck everyone

```html
<!DOCTYPE html>
<html lang="en">
<head>
<meta charset="utf-8">
<title>Tilda &amp; Rook Breeze Competition</title>
<link rel="stylesheet" href="https://fonts.googleapis.com/css2?family=Open+Sans:wght@300;400;700;800&family=Roboto+Condensed:wght@400;700&family=Passion+One&family=Kaushan+Script&family=Permanent+Marker&display=swap">
<style>
  :root {
    --stage: #e4e4e4;
    --paper: #f4ede0;
    --paper-edge: #e9dcc6;
    --brown: #4a2c20;
    --ink: #2e2a27;
    --orange: #e8662a;
    --orange-dark: #c9521c;
    --white: #ffffff;
    --panel: #f6f3ee;
    --terms: #6b645d;
    --blue-dot: #3b5bc4;
    --purple-dot: #b42fd6;
  }
  * { box-sizing: border-box; margin: 0; padding: 0; }
  html, body { width: 1200px; height: 1200px; overflow: hidden; }
  body { background: var(--stage); position: relative; font-family: "Open Sans", sans-serif; }

  .poster {
    position: absolute; left: 156px; top: 30px; width: 888px; height: 1140px;
    background: linear-gradient(180deg, var(--paper) 0%, #f7f1e6 50%, var(--paper-edge) 100%);
    overflow: hidden;
  }

  .brand { position: absolute; left: 70px; top: 44px; width: 150px; text-align: center; }
  .brand-dot { width: 70px; height: 70px; border-radius: 50%; background: var(--orange); margin: 0 auto 6px; }
  .brand-name { font-family: "Open Sans", sans-serif; font-weight: 800; font-size: 26px; color: var(--orange); line-height: 1; }
  .brand-tag { font-size: 11px; color: var(--orange); margin-top: 3px; }

  .title { position: absolute; right: 58px; top: 44px; text-align: right; color: var(--brown); }
  .title-main { font-weight: 800; font-size: 50px; letter-spacing: -0.5px; line-height: 1.1; }
  .title-sub { font-weight: 300; font-size: 44px; letter-spacing: 0.32em; margin-right: -0.32em; line-height: 1.2; color: var(--ink); }

  .food-photo {
    position: absolute; left: 10px; top: 205px; width: 872px; height: 720px;
    background:
      radial-gradient(ellipse 30% 28% at 44% 30%, #6b4a2a 0%, #8a6a3f 55%, rgba(138,106,63,0) 100%),
      radial-gradient(ellipse 14% 12% at 78% 20%, #7a1e14 0%, #b8311f 60%, rgba(184,49,31,0) 100%),
      radial-gradient(ellipse 40% 45% at 50% 45%, #9c7b52 0%, rgba(156,123,82,0.6) 60%, rgba(244,237,224,0) 100%);
  }
  .phone-photo {
    position: absolute; left: 440px; top: 458px; width: 446px; height: 478px;
    border-radius: 46px 46px 40px 110px;
    background: linear-gradient(160deg, #e9e4dc 0%, #5a4a30 22%, #6f7a3a 50%, #4c3a22 72%, #d9b99a 100%);
  }

  .social { position: absolute; border-radius: 50%; }
  .social-a { left: 596px; top: 808px; width: 62px; height: 62px; background: var(--blue-dot); }
  .social-share { left: 666px; top: 826px; width: 62px; height: 62px; background: var(--orange); display: flex; align-items: center; justify-content: center; }
  .social-b { left: 734px; top: 790px; width: 62px; height: 62px; background: var(--purple-dot); }

  .prize-sign {
    position: absolute; left: 40px; top: 212px; width: 388px; height: 340px;
    background: linear-gradient(180deg, var(--orange) 0%, var(--orange-dark) 100%);
    transform: rotate(-3deg);
    box-shadow: 0 4px 10px rgba(0,0,0,0.25);
    text-align: center; padding-top: 10px;
  }
  .prize-win { font-family: "Passion One", sans-serif; font-size: 138px; line-height: 0.85; color: var(--white); letter-spacing: 4px; }
  .prize-amount { font-family: "Passion One", sans-serif; font-size: 112px; line-height: 0.85; color: var(--white); }
  .prize-label { font-family: "Permanent Marker", "Kaushan Script", cursive; font-size: 42px; color: var(--brown); line-height: 1.1; margin-top: 4px; }
  .prize-note { font-family: "Roboto Condensed", sans-serif; font-size: 18px; color: var(--white); line-height: 1.25; margin-top: 4px; }

  .entry-panel {
    position: absolute; left: 62px; top: 562px; width: 344px; height: 380px;
    background: var(--panel); box-shadow: 0 2px 8px rgba(0,0,0,0.2);
    padding: 16px 16px 0 20px;
  }
  .entry-heading { font-family: "Kaushan Script", cursive; font-size: 30px; color: var(--orange); margin-bottom: 8px; }
  .entry-steps { list-style: none; font-family: "Roboto Condensed", sans-serif; font-size: 14px; color: var(--ink); line-height: 1.3; }
  .entry-steps li { display: flex; gap: 10px; align-items: flex-start; margin-bottom: 12px; }
  .step-num {
    flex: 0 0 26px; height: 26px; border-radius: 50%; background: var(--orange);
    color: var(--white); font-weight: 700; font-size: 16px; display: flex; align-items: center; justify-content: center;
  }
  .step-text { padding-top: 3px; }
  .entry-dates { font-family: "Kaushan Script", cursive; font-size: 15px; color: var(--orange); text-align: center; white-space: nowrap; margin-top: 6px; }

  .terms { position: absolute; left: 58px; top: 958px; width: 796px; font-size: 9.6px; line-height: 1.3; color: var(--terms); }
  .terms p { margin-bottom: 7px; }
  .terms strong { color: var(--ink); }
</style>
</head>
<body>
<main class="poster">
  <div class="food-photo" role="img" aria-label="Photo of a bowl of beef noodle soup with herbs, chilli and sauces on a wooden board"></div>
  <div class="phone-photo" role="img" aria-label="Photo of a hand holding a smartphone photographing the noodle soup"></div>

  <div class="social social-a" role="img" aria-label="Snapboard"></div>
  <div class="social social-share" role="img" aria-label="Share">
    <svg width="32" height="32" viewBox="0 0 34 34" aria-hidden="true">
      <line x1="9" y1="17" x2="25" y2="8" stroke="#fff" stroke-width="3"/>
      <line x1="9" y1="17" x2="25" y2="26" stroke="#fff" stroke-width="3"/>
      <circle cx="9" cy="17" r="5" fill="#fff"/>
      <circle cx="25" cy="8" r="5" fill="#fff"/>
      <circle cx="25" cy="26" r="5" fill="#fff"/>
    </svg>
  </div>
  <div class="social social-b" role="img" aria-label="Lensly"></div>

  <header class="brand">
    <div class="brand-dot"></div>
    <div class="brand-name">Lanh Bowl</div>
    <div class="brand-tag">Vietnamese Noodle House</div>
  </header>

  <h1 class="title">
    <span class="title-main">TILDA &amp; ROOK BREEZE</span><br>
    <span class="title-sub">COMPETITION</span>
  </h1>

  <section class="prize-sign">
    <div class="prize-win">WIN</div>
    <div class="prize-amount">$100</div>
    <div class="prize-label">Food Voucher</div>
    <p class="prize-note">Share your photos on<br>Snapboard or Lensly to WIN!</p>
  </section>

  <section class="entry-panel">
    <h2 class="entry-heading">To enter, simply:</h2>
    <ol class="entry-steps">
      <li><span class="step-num">1</span><span class="step-text">Like our Snapboard page or follow us on Lensly</span></li>
      <li><span class="step-num">2</span><span class="step-text">Take an original photo of any item(s) of our food</span></li>
      <li><span class="step-num">3</span><span class="step-text">Post your photo(s) to our Snapboard page or Lensly page, must use hashtags #tildaandrook #tildaandbreeze</span></li>
      <li><span class="step-num">4</span><span class="step-text">Be as creative as you'd like, and the TWO BEST photos voted by the Tilda and Rook team will receive a $100 Food Voucher.</span></li>
    </ol>
    <p class="entry-dates">1st AUGUST 2017 thru AUGUST 31st 2017</p>
  </section>

  <footer class="terms">
    <p><strong>Terms &amp; conditions:</strong><br>
    The competition opens 9:00am on Tuesday 1st and closes at 11:59pm Thursday 31st August. Judging of entries will be completed at the Lanh Bowl Quarry St store by 9:00pm the following Tuesday and the winners name and entry will be announced via Snapboard and Lensly post at 12:00pm Wednesday, September 6, 2017.</p>
    <p>All entries must not have been used in previous Lanh Bowl competitions and the number of entries an Eligible Entrant may send is not limited, provided each entry is different and tagged correctly. This is a game of skill. Each entry will be individually judged, based upon individual creative merit. The entry image must be the Eligible Entrant's original piece. Employees of Lanh Bowl and immediate families are ineligible to enter the competition.</p>
    <p>The prize is valued at $100 per winner, to be used within 6 months of receipt. The prize is not transferable &amp; cannot be converted to cash. The Promoter is not liable for any loss or damage which is suffered or incurred by any person, including but not limited to indirect or consequential loss, or for personal injury suffered or sustained during the course of accepting or using the prize, except for any liability which cannot be excluded by law. By entering the competition, each entrant acknowledges their entry content may be used for printing, broadcast, publicity and promotional purposes, including but not limited to the Promoter's websites and social media accounts without compensation.</p>
    <p>The Promoter is Lanh Bowl Pty Ltd (ABN 41 702 385 916) Shop 7/ 18 Harbour Lane Marrick NSW 2140. Ground Floor, Shop 2/ 505 Quarry St, Sydney NSW 2000.</p>
  </footer>
</main>
</body>
</html>
```